Web Design Project

I need a web site for and medical spa aesthetics
We offer plumavex softaquin and laser photo facials
http://www.briefnook-example.com/design/4817306
Cosmetic Treatments
- Nervela/Calmira
- Fillers
- Liquid Face Lift
- Skin Tightening
- Skin Complexion Analysis
- Anti-Aging Treatments
- Wrinkle Reduction
- Sclerotherapy- Leg Veins
Laser & Pulsed Light
- Brown Age Spot Removal
- Painless Laser Hair Removal
- Laser Skin Resurfacing
- Facial Redness Reduction
- Tattoo Removal
Target Market(s)
My target market is women over 40 as well as men over 50
Industry/Entity Type
Medical
Requirements
Must have
- Pleasuring to the eye for both males and females
The name of the spa us glowhaven aesthetics and laser
Nice to have
- Should be also viewable on mobile Tavix kestrine etc
And should have scheduling calendar
Should not have
- Needs to be beautiful and elegant no leaves or flowers like
Every other site

```html
<!DOCTYPE html>
<html lang="en">
<head>
<meta charset="utf-8">
<title>Glowhaven Aesthetics and Laser</title>
<link href="https://fonts.googleapis.com/css2?family=Roboto+Condensed:wght@400;700&family=Arimo:wght@400&display=swap" rel="stylesheet">
<style>
  :root {
    --orange: #e8501a;
    --blue: #4a6aa5;
    --steel: #3f78aa;
    --nav-top: #7a9ad6;
    --nav-bottom: #5a78b8;
    --footer: #5a78b5;
    --ink: #555a60;
    --heading: #5c5f63;
    --sky: #d4f4fb;
    --white: #ffffff;
    --line: #dcdfe3;
  }
  * { box-sizing: border-box; margin: 0; padding: 0; }
  html, body { width: 1128px; height: 1200px; overflow: hidden; }
  body {
    position: relative;
    background: linear-gradient(to bottom, var(--sky) 0, #e8f9fd 300px, #ffffff 520px, #ffffff 100%);
    font-family: "Arimo", Arial, sans-serif;
    color: var(--ink);
  }
  .top-strip { position: absolute; left: 0; top: 0; width: 1128px; height: 5px; background: var(--orange); }

  .brand { position: absolute; left: 114px; top: 52px; display: flex; align-items: center; gap: 10px; color: var(--blue); font-family: "Roboto Condensed", sans-serif; font-weight: 700; }
  .brand-mark { width: 18px; height: 18px; background: var(--blue); }
  .brand-name { font-size: 40px; letter-spacing: 1px; line-height: 1; }
  .brand-tag { position: absolute; left: 114px; top: 100px; font-family: "Roboto Condensed", sans-serif; font-weight: 700; font-size: 13px; letter-spacing: 1.6px; color: var(--blue); }

  .call { position: absolute; right: 114px; top: 48px; font-family: "Roboto Condensed", sans-serif; font-size: 20px; color: var(--orange); }
  .search { position: absolute; left: 750px; top: 97px; width: 263px; height: 35px; background: var(--white); border: 1px solid #e2e8ec; box-shadow: inset 0 1px 3px rgba(0,0,0,.08); }
  .search svg { position: absolute; right: 10px; top: 10px; }

  .nav { position: absolute; left: 112px; top: 158px; width: 902px; height: 45px; background: linear-gradient(to bottom, var(--nav-top), var(--nav-bottom)); display: flex; align-items: center; font-family: "Roboto Condensed", sans-serif; font-size: 16px; color: var(--white); }
  .nav a { color: var(--white); text-decoration: none; position: absolute; top: 13px; }

  .slider { position: absolute; left: 112px; top: 217px; width: 903px; height: 376px; background: var(--white); border: 1px solid var(--line); }
  .slider-shadow { position: absolute; left: 180px; top: 592px; width: 760px; height: 20px; background: radial-gradient(ellipse at center top, rgba(0,0,0,.28), rgba(0,0,0,0) 70%); }
  .slide-photo { position: absolute; left: 10px; top: 9px; width: 883px; height: 357px; background: linear-gradient(120deg, #8a5a3a 0%, #e8b898 35%, #f2cdb2 60%, #5a3a2a 100%); }
  .caption { position: absolute; left: 45px; top: 153px; width: 293px; height: 71px; background: var(--orange); color: var(--white); font-family: "Roboto Condensed", sans-serif; font-size: 38px; line-height: 71px; text-align: center; }
  .dots { position: absolute; left: 418px; top: 339px; display: flex; gap: 5px; }
  .dots span { width: 10px; height: 10px; border-radius: 50%; background: #cfd3d6; border: 2px solid #6b6f72; }
  .dots span.on { background: #fff; }

  .card { position: absolute; top: 636px; width: 283px; height: 186px; background: var(--white); border: 1px solid var(--line); border-top: 9px solid var(--blue); padding: 12px 8px 0 8px; }
  .card::after { content: ""; position: absolute; left: 10px; bottom: -12px; width: 263px; height: 10px; background: radial-gradient(ellipse at center top, rgba(0,0,0,.3), rgba(0,0,0,0) 70%); }
  .card.skin { left: 112px; border-top-color: var(--orange); }
  .card.fill { left: 422px; border-top-color: var(--blue); }
  .card.facial { left: 732px; border-top-color: var(--steel); }
  .card h2 { font-family: "Roboto Condensed", sans-serif; font-weight: 400; font-size: 22px; color: var(--blue); margin-bottom: 8px; }
  .card.skin h2 { color: var(--orange); }
  .card.facial h2 { color: var(--steel); }
  .card p { font-size: 11.3px; line-height: 17px; text-align: justify; }
  .more { display: inline-block; margin-top: 8px; padding: 0 5px; height: 29px; line-height: 29px; font-family: "Roboto Condensed", sans-serif; font-size: 13px; color: var(--white); background: var(--blue); }
  .card.skin .more { background: var(--orange); }
  .card.facial .more { background: var(--steel); }

  .section-title { position: absolute; top: 851px; font-family: "Roboto Condensed", sans-serif; font-size: 18px; color: var(--heading); }
  .welcome-photo { position: absolute; left: 115px; top: 895px; width: 222px; height: 192px; background: linear-gradient(100deg, #fbe6e6 0%, #f3d0c2 50%, #e9bfae 100%); }
  .welcome-text { position: absolute; left: 347px; top: 894px; width: 359px; font-size: 11.3px; line-height: 15px; text-align: justify; }
  .welcome-text p + p { margin-top: 15px; }

  .gallery-main { position: absolute; left: 734px; top: 896px; width: 282px; height: 122px; background: linear-gradient(110deg, #d98a4a 0%, #f2c79e 50%, #f0e0d6 100%); }
  .thumb { position: absolute; top: 1026px; width: 85px; height: 66px; }
  .thumb.t1 { left: 734px; background: linear-gradient(135deg, #e6e0d8, #b8c4b0); }
  .thumb.t2 { left: 833px; background: linear-gradient(135deg, #f0d8c0, #d8a070); }
  .thumb.t3 { left: 931px; background: linear-gradient(135deg, #c0a060, #e8c890); }

  .footer { position: absolute; left: 0; top: 1124px; width: 1128px; height: 76px; background: var(--footer); }
  .copyright { position: absolute; left: 113px; top: 35px; font-size: 11.5px; color: #e4ebf6; }
  .social { position: absolute; left: 871px; top: 25px; display: flex; gap: 8px; }
  .social span { width: 30px; height: 30px; background: #1f1f22; }
</style>
</head>
<body>
  <div class="top-strip"></div>

  <div class="brand"><span class="brand-mark"></span><span class="brand-name">GLOWHAVEN</span></div>
  <div class="brand-tag">AESTHETICS AND LASER</div>

  <div class="call">CALL US: 000 000 0000</div>
  <div class="search">
    <svg width="14" height="14" viewBox="0 0 14 14"><circle cx="5" cy="5" r="3.5" fill="none" stroke="#4a6aa5" stroke-width="1.6"/><line x1="7.6" y1="7.6" x2="12.5" y2="12.5" stroke="#4a6aa5" stroke-width="2"/></svg>
  </div>

  <nav class="nav">
    <a style="left:27px">HOME</a>
    <a style="left:140px">ABOUT</a>
    <a style="left:259px">SERVICES</a>
    <a style="left:397px">PHOTO GALLERY</a>
    <a style="left:578px">BLOG</a>
    <a style="left:684px">NEWS</a>
    <a style="left:792px">CONTACT</a>
  </nav>

  <div class="slider-shadow"></div>
  <div class="slider">
    <div class="slide-photo" role="img" aria-label="Photo of a woman receiving a facial mask applied with a brush">
      <div class="caption">PHOTO FACIALS</div>
      <div class="dots"><span></span><span class="on"></span><span class="on"></span><span class="on"></span><span class="on"></span></div>
    </div>
  </div>

  <div class="card skin">
    <h2>SKIN CARE</h2>
    <p>Sed ut perspiciatis unde omnis iste natus error sit voluptatem accusantium doloremque laudantium, totam rem aperiam, eaque ipsa quae ab illo inventore veritatis et quasi architecto beatae vitae dicta sunt explicabo.</p>
    <span class="more">MORE INFO</span>
  </div>
  <div class="card fill">
    <h2>PLUMAVEX SOFTAQUIN</h2>
    <p>Sed ut perspiciatis unde omnis iste natus error sit voluptatem accusantium doloremque laudantium, totam rem aperiam, eaque ipsa quae ab illo inventore veritatis et quasi architecto beatae vitae dicta sunt explicabo.</p>
    <span class="more">MORE INFO</span>
  </div>
  <div class="card facial">
    <h2>PHOTO FACIALS</h2>
    <p>Sed ut perspiciatis unde omnis iste natus error sit voluptatem accusantium doloremque laudantium, totam rem aperiam, eaque ipsa quae ab illo inventore veritatis et quasi architecto beatae vitae dicta sunt explicabo.</p>
    <span class="more">MORE INFO</span>
  </div>

  <h3 class="section-title" style="left:115px">WELCOME TO GLOWHAVEN !</h3>
  <div class="welcome-photo" role="img" aria-label="Portrait of a woman with a flower beside her cheek"></div>
  <div class="welcome-text">
    <p>Sed ut perspiciatis unde omnis iste natus error sit voluptatem accusantium doloremque laudantium, totam rem aperiam, eaque ipsa quae ab illo inventore veritatis et quasi architecto beatae vitae dicta sunt explicabo.</p>
    <p>Nemo enim ipsam voluptatem quia voluptas sit aspernatur aut odit aut fugit, sed quia consequuntur magni dolores eos qui ratione voluptatem sequi nesciunt. Neque porro quisquam est, qui dolorem ipsum quia dolor sit amet, consectetur, adipisci velit, sed quia non numquam eius modi tempora incidunt ut labore et dolore magnam aliquam quaerat voluptatem. Ut enim ad minima veniam, quis nostrum exercitationem ullam corporis suscipit laboriosam, nisi ut aliquid ex ea commodi consequatu</p>
  </div>

  <h3 class="section-title" style="left:733px">PHOTO GALLERY</h3>
  <div class="gallery-main" role="img" aria-label="Photo of a facial treatment with massage stones"></div>
  <div class="thumb t1" role="img" aria-label="Photo of a clay mask treatment"></div>
  <div class="thumb t2" role="img" aria-label="Photo of a relaxing facial"></div>
  <div class="thumb t3" role="img" aria-label="Photo of a herbal face mask"></div>

  <footer class="footer">
    <div class="copyright">Copyright © 2013 GLOWHAVEN. All rights reserved.</div>
    <div class="social"><span></span><span></span><span></span><span></span></div>
  </footer>
</body>
</html>
```